Brisa Lumen Systems Corp Business Cards

Business cards to match the logo.

Company is a start up water technology company that has developed a patented system using centrifugal force to separate waste from municipal waste water to produce crystal clear clean water. Product sell starting at 2 million to governments both in the US and international.

Business cards should have a professional look with the target generally engineers.

Target Market(s)

Engineers, Government officials and investors

Industry/Entity Type

Water Treatment

Contact Information for Business Card

Business cards design will be used for 6 to 8 people with job titles. Can use the quote "If there is magic in the planet, it is contained in water." but not required to use quote. Should follow theme of Logo

Font styles to use
Other font styles liked:
• match logo font

Requirements
Nice to have
• Colors to match Logo. Business cards to match style of flow of Logo.
• Emphasis on clean look not a busy look. Clean flowing water.
Should not have
• Pictures of industrial equipment or wastewater

```html
<!DOCTYPE html>
<html lang="en">
<head>
<meta charset="utf-8">
<title>Brisa Lumen Systems Corp Business Cards</title>
<link href="https://fonts.googleapis.com/css2?family=Playfair+Display:wght@400;600&family=Work+Sans:wght@400&display=swap" rel="stylesheet">
<style>
  :root {
    --backdrop: #1c1c1e;
    --paper: #ffffff;
    --deep-blue: #17557f;
    --bright-blue: #2ba7e0;
    --name-blue: #1f6db5;
    --ink: #3a3a3a;
  }
  * { margin: 0; padding: 0; box-sizing: border-box; }
  html, body { width: 1200px; height: 897px; overflow: hidden; background: var(--backdrop); }
  .canvas { position: relative; width: 1200px; height: 897px; }
  .card {
    position: absolute; left: 303px; width: 595px; height: 339px;
    border-radius: 18px; overflow: hidden;
  }
  .card-front { top: 92px; background: var(--paper); }
  .card-back { top: 469px; background: var(--deep-blue); }
  .info-band {
    position: absolute; left: 0; right: 0; top: 214px; bottom: 0;
    background: var(--deep-blue);
    border-top: 4px solid var(--bright-blue);
  }
  .brand-name {
    position: absolute; left: 39px; top: 54px;
    font-family: "Playfair Display", serif; font-weight: 400;
    font-size: 25px; color: var(--deep-blue); letter-spacing: 0.3px;
  }
  .person { position: absolute; right: 39px; top: 34px; text-align: right; }
  .person-name {
    font-family: "Playfair Display", serif; font-weight: 600;
    font-size: 23px; line-height: 28px; color: var(--name-blue); letter-spacing: 0.5px;
  }
  .person-title {
    font-family: "Work Sans", sans-serif; font-size: 13px; color: var(--ink);
    margin-top: 4px; letter-spacing: 0.5px;
  }
  .address {
    position: absolute; left: 39px; top: 270px; font-style: normal;
    font-family: "Work Sans", sans-serif; font-size: 13px; line-height: 17px;
    color: var(--paper); letter-spacing: 0.3px;
  }
  .contact {
    position: absolute; right: 36px; top: 253px; list-style: none;
    font-family: "Work Sans", sans-serif; font-size: 13px; line-height: 17px;
    color: var(--paper); text-align: right; letter-spacing: 0.3px;
  }
  .contact li { display: flex; justify-content: flex-end; align-items: center; gap: 10px; }
  .contact svg { width: 9px; height: 9px; flex: none; }
  .back-brand {
    position: absolute; left: 0; right: 0; top: 152px; text-align: center;
    font-family: "Playfair Display", serif; font-weight: 400;
    font-size: 34px; color: var(--paper); letter-spacing: 1px;
  }
</style>
</head>
<body>
<main class="canvas">
  <section class="card card-front">
    <div class="info-band"></div>
    <div class="brand-name">Brisa Lumen Systems</div>
    <div class="person">
      <div class="person-name">DANIEL FENWICK</div>
      <div class="person-title">Founder</div>
    </div>
    <address class="address">480 Harbor Crest Rd.<br>Coral Bay, FL 33100</address>
    <ul class="contact">
      <li>555-214-7730
        <svg viewBox="0 0 10 10" aria-hidden="true"><path d="M2,1 L4,1 L4.5,3 L3.3,3.8 C3.8,5 5,6.2 6.2,6.7 L7,5.5 L9,6 L9,8 C5,8.5 1.5,5 2,1 Z" fill="var(--bright-blue)"/></svg>
      </li>
      <li>hello@brisalumen.com
        <svg viewBox="0 0 10 10" aria-hidden="true"><rect x="1" y="2.5" width="8" height="5.5" fill="none" stroke="var(--bright-blue)"/><path d="M1,2.5 L5,5.5 L9,2.5" fill="none" stroke="var(--bright-blue)"/></svg>
      </li>
      <li>www.BrisaLumen.com
        <svg viewBox="0 0 10 10" aria-hidden="true"><circle cx="5" cy="5" r="4" fill="none" stroke="var(--bright-blue)"/><path d="M1,5 H9 M5,1 C3,3.5 3,6.5 5,9 C7,6.5 7,3.5 5,1" fill="none" stroke="var(--bright-blue)" stroke-width="0.8"/></svg>
      </li>
    </ul>
  </section>

  <section class="card card-back">
    <div class="back-brand">BRISA LUMEN SYSTEMS</div>
  </section>
</main>
</body>
</html>
```